Design the Keystone HR business card for my new business

I've just had a logo designed (attached) for my new business doing HR consulting. I'm a one person operation at this stage, my aim is to provide support and help to small to medium sized businesses with their people objectives or issues.

I'm not really into anything overly flashy, I'm not a PR or marketing agency. I'd like my card to look modern, professional and not gimmicky.

I'm thinking black front (to go with logo), double sided with details on the back, maybe in a different colour?

Logo attached in several different formats.

Front of the card to have logo and added text: People and Development Solutions

Back of the card to also feature logo in some way and say:
Megan Tulloch
PO Box (TBA)
Marrowvale QLD 4391
0438 512 976
megan@keystonehr.com.au
www.keystonehr.com.au

Target Market(s)

Small to medium businesses / business owners.

Industry/Entity Type

Marketing

Requirements
Must have
• Double sided business card.
Should not have
• Anything overly gimmicky.

```html
<!DOCTYPE html>
<html lang="en">
<head>
<meta charset="utf-8">
<title>Keystone HR Consulting – Business Card</title>
<link rel="stylesheet" href="https://fonts.googleapis.com/css2?family=Questrial&family=Open+Sans:wght@400;600&display=swap">
<style>
  :root {
    --page: #ffffff;
    --front-bg: #000000;
    --back-bg: #999999;
    --mark-front: #b3b3b3;
    --mark-back: #a9a9a9;
    --ink-light: #ffffff;
    --rule: #d9d9d9;
    --accent: #f5a623;
    --wave-light: #e6e6e6;
    --wave-mid: #8c8c8c;
  }
  html, body {
    margin: 0;
    padding: 0;
    width: 1200px;
    height: 997px;
    overflow: hidden;
    background: var(--page);
  }
  .card-sheet {
    display: block;
    width: 1200px;
    height: 997px;
  }
  .card-front-shape { fill: var(--front-bg); }
  .card-back-shape { fill: var(--back-bg); }
  .mark-front { fill: var(--mark-front); }
  .mark-back { fill: var(--mark-back); }
  .brand-name {
    font-family: "Questrial", sans-serif;
    font-weight: 400;
    fill: var(--ink-light);
  }
  .tagline {
    font-family: "Open Sans", sans-serif;
    font-weight: 600;
    font-size: 21px;
    fill: var(--ink-light);
  }
  .person-name {
    font-family: "Open Sans", sans-serif;
    font-weight: 400;
    font-size: 23px;
    fill: var(--ink-light);
  }
  .contact {
    font-family: "Open Sans", sans-serif;
    font-weight: 400;
    font-size: 17px;
    fill: var(--ink-light);
  }
  .contact-label {
    font-family: "Open Sans", sans-serif;
    font-size: 20px;
    fill: var(--accent);
  }
  .detail-rule {
    stroke: var(--rule);
    stroke-width: 1.5;
  }
</style>
</head>
<body>
<svg class="card-sheet" viewBox="0 0 1200 997" xmlns="http://www.w3.org/2000/svg">
  <defs>
    <linearGradient id="wave-front" x1="0" y1="0" x2="1" y2="0">
      <stop offset="0" stop-color="var(--wave-mid)" stop-opacity="0.2"/>
      <stop offset="0.6" stop-color="var(--wave-light)" stop-opacity="0.55"/>
      <stop offset="1" stop-color="var(--wave-mid)" stop-opacity="0.3"/>
    </linearGradient>
    <linearGradient id="wave-back" x1="0" y1="0" x2="1" y2="0">
      <stop offset="0" stop-color="var(--wave-light)" stop-opacity="0.6"/>
      <stop offset="1" stop-color="var(--wave-light)" stop-opacity="0.1"/>
    </linearGradient>
  </defs>

  <!-- Front side -->
  <g class="card-front">
    <path class="card-front-shape" d="M59 62 H491 V121 H521 Q537 121 537 140 V900 Q537 935 500 935 H59 Z"/>
    <path role="img" aria-label="Flowing fine-line wave decoration along the right edge"
          fill="url(#wave-front)"
          d="M500 128 Q537 128 537 150 V900 Q537 935 500 935 H285 Q420 850 490 700 Q530 560 480 420 Q440 300 500 128 Z"/>
    <circle class="mark-front" cx="257" cy="257" r="145"/>
    <text class="brand-name" x="79" y="598" font-size="108">Keystone</text>
    <text class="brand-name" x="89" y="681" font-size="54">HR Consulting</text>
    <text class="tagline" x="81" y="726">People and Development Solutions</text>
  </g>

  <!-- Back side -->
  <g class="card-back">
    <path class="card-back-shape" d="M693 58 H1122 V935 H690 Q647 935 647 895 V150 Q647 121 667 121 H693 Z"/>
    <path role="img" aria-label="Flowing fine-line wave decoration along the left edge"
          fill="url(#wave-back)"
          d="M667 121 Q700 121 705 160 Q720 320 690 470 Q660 620 720 760 Q760 860 820 935 H690 Q647 935 647 895 V150 Q647 121 667 121 Z"/>
    <circle class="mark-back" cx="911" cy="280" r="152"/>
    <text class="brand-name" x="676" y="519"><tspan font-size="54">keystone</tspan><tspan font-size="32" dx="6">HR Consulting</tspan></text>

    <text class="person-name" x="927" y="600" text-anchor="middle">Megan Tulloch</text>

    <line class="detail-rule" x1="660" y1="651" x2="1122" y2="651"/>
    <line class="detail-rule" x1="650" y1="703" x2="1122" y2="703"/>
    <line class="detail-rule" x1="841" y1="703" x2="841" y2="788"/>
    <line class="detail-rule" x1="660" y1="788" x2="1122" y2="788"/>
    <line class="detail-rule" x1="700" y1="826" x2="1122" y2="826"/>

    <text class="contact-label" x="858" y="686">e.</text>
    <text class="contact" x="880" y="686">megan@keystonehr.com.au</text>

    <text class="contact-label" x="665" y="753">ph.</text>
    <text class="contact" x="700" y="753">0438 512 976</text>

    <text class="contact-label" x="858" y="731">a.</text>
    <text class="contact" x="880" y="731">PO Box (TBA)</text>
    <text class="contact" x="888" y="760">Marrowvale QLD 4391</text>

    <text class="contact-label" x="858" y="813">w.</text>
    <text class="contact" x="888" y="813">www.keystonehr.com.au</text>
  </g>
</svg>
</body>
</html>
```